KMRT timeline design

We need a facebook design for our established business which is Australia wide however based in Melbourne. We are a young team of Financial Planners who specialize in Insurance and Basic super advice for people like us.

We are people who help our clients get things done in a timely and cost effective manner whilst having a good time and a laugh along the way.

We do not want it to feel like the standard financial facebook page at all! We would like this to have a consistent feel with our new e-brochure which i have attached from a color and font perspective.

We would also like it to be very easy for people to be able to tell what we do from looking at the page

Reason: Would like time to respond to preferred designs and have re-works done before comitting

Target Market(s)

We work best with client from 25-40 who are time poor singles, young families and self-made entrepreneurs

Industry/Entity Type

Financial

```html
<!DOCTYPE html>
<html lang="en">
<head>
<meta charset="utf-8">
<title>KMRT Timeline Cover</title>
<link rel="stylesheet" href="https://fonts.googleapis.com/css2?family=Roboto:wght@300;400;700&display=swap">
<style>
  :root {
    --brand-green: #6cc04a;
    --brand-green-dark: #4c9a30;
    --cover-dark: #231f20;
    --cover-mid: #4a4546;
    --ink-white: #ffffff;
    --page-white: #ffffff;
    --button-bg: #f5f6f7;
    --button-border: #9aa0ab;
    --button-text: #333333;
    --frame-border: #c9ccd2;
    --photo-light: #cfcfcf;
    --photo-dark: #5a5a5a;
  }
  * { margin: 0; padding: 0; box-sizing: border-box; }
  html, body {
    width: 1200px; height: 564px; overflow: hidden;
    background: var(--page-white);
    font-family: "Roboto", Arial, sans-serif;
  }
  .timeline { position: relative; width: 1200px; height: 564px; overflow: hidden; }
  .cover {
    position: absolute; left: 0; top: 0; width: 1200px; height: 444px;
  }
  .cover-art { position: absolute; inset: 0; }
  .advice-heading {
    position: absolute; left: 28px; top: 94px;
    color: var(--brand-green); font-weight: 300;
    font-size: 37px; line-height: 38px; letter-spacing: 0.5px;
    text-transform: uppercase;
  }
  .step-label {
    position: absolute; top: 237px; width: 240px; margin-left: -120px;
    text-align: center; color: var(--ink-white);
    font-size: 22px; font-weight: 400; letter-spacing: 0.3px;
  }
  .step-discovery { left: 335px; }
  .step-strategy { left: 568px; }
  .step-implementation { left: 802px; }
  .tagline {
    position: absolute; left: 282px; top: 327px;
    color: var(--brand-green); font-weight: 300;
    font-size: 38px; line-height: 45px; text-transform: uppercase;
  }
  .profile-frame {
    position: absolute; left: 28px; top: 278px; width: 238px; height: 236px;
    background: var(--page-white); border: 1px solid var(--frame-border);
    padding: 5px;
  }
  .profile-mark {
    width: 100%; height: 100%; background: var(--cover-dark);
    display: flex; flex-direction: column; align-items: center; justify-content: center; gap: 18px;
  }
  .profile-square { width: 78px; height: 78px; background: var(--brand-green); }
  .profile-name {
    color: var(--ink-white); font-weight: 700; font-size: 40px; letter-spacing: 2px;
  }
  .page-actions {
    position: absolute; top: 467px; left: 821px; display: flex; gap: 18px;
  }
  .action-button {
    height: 34px; border: 1px solid var(--button-border); background: var(--button-bg);
    color: var(--button-text); font-weight: 700; font-size: 17px;
    display: flex; align-items: center; padding: 0 11px;
  }
  .action-group { display: flex; }
  .action-settings { border-left: none; padding: 0 12px; gap: 8px; }
  .caret { width: 0; height: 0; border-left: 6px solid transparent; border-right: 6px solid transparent; border-top: 6px solid #4b67a1; }
</style>
</head>
<body>
<div class="timeline">
  <section class="cover">
    <svg class="cover-art" width="1200" height="444" viewBox="0 0 1200 444">
      <defs>
        <radialGradient id="coverGlow" cx="0.4" cy="0.45" r="0.7">
          <stop offset="0" stop-color="var(--cover-mid)"/>
          <stop offset="1" stop-color="var(--cover-dark)"/>
        </radialGradient>
        <linearGradient id="photoTone" x1="0" y1="0" x2="1" y2="1">
          <stop offset="0" stop-color="var(--photo-light)"/>
          <stop offset="1" stop-color="var(--photo-dark)"/>
        </linearGradient>
      </defs>
      <rect width="1200" height="444" fill="url(#coverGlow)"/>
      <path d="M954 0 H980 V320 C980 405 905 444 830 444 H800 C885 432 954 398 954 318 Z" fill="var(--brand-green)"/>
      <path role="img" aria-label="Black and white portrait of a smiling team member" d="M978 0 H1200 V444 H830 C905 444 978 405 978 320 Z" fill="url(#photoTone)"/>

      <g class="icon-discovery" transform="translate(335 141)">
        <circle r="82" fill="var(--brand-green)"/>
        <circle cy="-18" r="30" fill="var(--ink-white)" stroke="var(--cover-dark)" stroke-width="3"/>
        <rect x="-16" y="10" width="32" height="12" fill="var(--ink-white)" stroke="var(--cover-dark)" stroke-width="3"/>
        <rect x="-14" y="22" width="28" height="8" fill="var(--ink-white)" stroke="var(--cover-dark)" stroke-width="3"/>
        <rect x="-12" y="30" width="24" height="8" fill="var(--ink-white)" stroke="var(--cover-dark)" stroke-width="3"/>
        <path d="M-6 40 H6 L3 46 H-3 Z" fill="var(--ink-white)"/>
      </g>

      <g class="icon-strategy" transform="translate(568 141)" fill="none" stroke="var(--ink-white)">
        <circle r="82" fill="var(--brand-green)" stroke="none"/>
        <circle cy="-4" r="36" stroke-width="8"/>
        <circle cy="-4" r="20" stroke-width="7"/>
        <circle cy="-4" r="6" fill="var(--ink-white)" stroke="none"/>
        <path d="M0 -4 L40 -44" stroke-width="5"/>
        <path d="M34 -50 L46 -38 M40 -54 L50 -44" stroke-width="4"/>
        <path d="M-24 30 L-32 50 M24 30 L32 50 M0 34 V52" stroke-width="5" stroke-linecap="round"/>
      </g>

      <g class="icon-implementation" transform="translate(802 141)" stroke="var(--ink-white)" stroke-linecap="round">
        <circle r="82" fill="var(--brand-green)" stroke="none"/>
        <path d="M-36 36 L26 -26" stroke-width="12"/>
        <circle cx="32" cy="-32" r="14" fill="var(--ink-white)" stroke="none"/>
        <path d="M32 -32 L46 -46" stroke="var(--brand-green)" stroke-width="9"/>
        <path d="M36 36 L-6 -6" stroke-width="12"/>
        <path d="M-8 -8 L-30 -30" stroke-width="6"/>
        <path d="M-30 -30 L-40 -40" stroke-width="10"/>
      </g>
    </svg>

    <h1 class="advice-heading">Our<br>Financial<br>Advice</h1>
    <p class="step-label step-discovery">DISCOVERY</p>
    <p class="step-label step-strategy">STRATEGY</p>
    <p class="step-label step-implementation">IMPLEMENTATION</p>
    <p class="tagline">Secure future,<br>enhanced lifestyle</p>
  </section>

  <div class="profile-frame">
    <div class="profile-mark">
      <span class="profile-square"></span>
      <span class="profile-name">KMRT</span>
    </div>
  </div>

  <nav class="page-actions">
    <span class="action-button">Update Info</span>
    <span class="action-group">
      <span class="action-button">Activity Log</span>
      <span class="action-button action-settings">
        <svg width="16" height="16" viewBox="0 0 16 16" aria-hidden="true">
          <circle cx="8" cy="8" r="5" fill="none" stroke="#333" stroke-width="3" stroke-dasharray="2.4 1.5"/>
          <circle cx="8" cy="8" r="2" fill="#333"/>
        </svg>
        <span class="caret"></span>
      </span>
    </span>
  </nav>
</div>
</body>
</html>
```